Cordova Exercise Phone Application Screen Design

We need a sharp professional design for a phone application. We specialize in Health and Fitness Software. This app will be a companion for www.MotionCraftHub.example.
We will be doing all backend and javascript work here and we need someone to create the HTML and CSS for the application which will be developed in Cordova.
For the contest we are submitting three screens. Once we award a winner we will give the winner the first oportunity to bid on the remaining 10 screens.
For the first step of the contest please do the page 1 and page 2 screen design, feel free to submit multiple designs. If we like your designs we will contact you and ask you to design the third page. Once that is done we would like to see the HTML and CSS for the three pages.
Page 1: Simple Home Page
Page 2: Client Search - The search is at the top and the results are below that. The Active | Inactive section is a selection (see https://brivolatech.example/radio-buttons-as-toggle-buttons-with-css/ for an example). Client A has their record expanded (that is what the triangle is). 136 stars should be 136 with Font-Awesome star after the number. To see what the graphs should look like please see the attached png. Then a list is below the stars and graphs.
Page 3/4: Step 1 of 3 - When the magnifying glass is selected a flyout with the search criteria comes out (page 3). Criteria is selected and the results are shown (page 4).
The default width should be 320 but the application should look good on all phones and tablets.
Please feel free to contact us with questions. The winner will get more work of a similar nature.

Target Market(s)
Physical Therapists
Font styles to use
Colors
Designer to choose colors to be used in the design.
Requirements
Must have
- Clean and easy to understand design. Look professional and uncluttered. Be easy to understand and use. Must have the logo at the top (just the MCH logo is fine)
Should not have
- Cartoonish look and feel.

```html
<!DOCTYPE html>
<html lang="en">
<head>
<meta charset="utf-8">
<title>Create Exercise Program – Step 1 of 3</title>
<link href="https://fonts.googleapis.com/css2?family=Roboto:wght@400;500;700&display=swap" rel="stylesheet">
<style>
  :root {
    --ink: #000000;
    --text: #333333;
    --white: #ffffff;
    --panel: #ececec;
    --green: #45c35a;
    --green-text: #3fbb4f;
    --badge: #e53935;
    --toggle-bg: #d9d9d9;
    --toggle-active: #6b6b6b;
    --rule: #cfcfcf;
    --chevron: #9a9a9a;
    --field-border: #a8a8a8;
  }
  * { box-sizing: border-box; margin: 0; padding: 0; }
  html, body {
    width: 1200px; height: 3352px; overflow: hidden;
    background: var(--white);
    font-family: "Roboto", Arial, sans-serif;
    color: var(--text);
  }
  .screen { position: relative; width: 1200px; height: 3352px; }

  /* Header */
  .app-header {
    position: absolute; left: 0; top: 0; width: 1200px; height: 224px;
    background: var(--ink); color: var(--white);
  }
  .brand {
    position: absolute; left: 72px; top: 40px; height: 128px;
    display: flex; align-items: center; gap: 20px;
  }
  .brand-mark { width: 28px; height: 28px; background: var(--white); }
  .brand-name { font-weight: 700; font-size: 64px; letter-spacing: 2px; color: var(--white); }
  .app-title {
    position: absolute; left: 368px; top: 28px; width: 640px;
    font-weight: 700; font-size: 68px; line-height: 84px; text-transform: uppercase;
  }
  .help-icon { position: absolute; left: 1016px; top: 48px; width: 120px; height: 120px; }

  /* Step controls */
  .step-panel {
    position: absolute; left: 0; top: 224px; width: 1200px; height: 648px;
    background: var(--panel);
  }
  .btn {
    position: absolute; height: 116px; display: flex; align-items: center; justify-content: center;
    font-weight: 700; font-size: 52px; text-transform: uppercase;
  }
  .btn-cancel { left: 72px; top: 44px; width: 312px; background: var(--white); border: 8px solid var(--ink); color: var(--ink); }
  .btn-next { left: 828px; top: 44px; width: 304px; background: var(--green); color: var(--white); }
  .step-label {
    position: absolute; left: 384px; top: 44px; width: 444px; height: 116px;
    display: flex; align-items: center; justify-content: center;
    color: var(--green-text); font-weight: 700; font-size: 56px;
  }
  .btn-view { left: 280px; top: 232px; width: 640px; background: var(--white); border: 8px solid var(--ink); color: var(--ink); gap: 24px; }
  .btn-view svg { width: 64px; height: 48px; }
  .count-badge {
    position: absolute; left: 248px; top: 200px; width: 72px; height: 72px; border-radius: 50%;
    background: var(--badge); color: var(--white); font-weight: 700; font-size: 44px;
    display: flex; align-items: center; justify-content: center;
  }
  .mode-toggle {
    position: absolute; left: 152px; top: 440px; width: 896px; height: 120px;
    background: var(--toggle-bg); border-radius: 16px; display: flex; align-items: center; padding: 0 12px;
    font-weight: 700; font-size: 52px; text-transform: uppercase; color: #555555;
  }
  .mode-option { height: 96px; display: flex; align-items: center; padding: 0 24px; border-radius: 12px; }
  .mode-option.is-active { background: var(--toggle-active); color: var(--white); }

  /* Filters */
  .field-label { position: absolute; color: var(--green-text); font-weight: 700; font-size: 60px; }
  .select {
    position: absolute; top: 1080px; height: 144px; border: 4px solid var(--field-border); border-radius: 16px;
    background: var(--white); display: flex; align-items: center; justify-content: space-between;
    padding: 0 36px; font-size: 60px; color: var(--text);
  }
  .select svg { width: 72px; height: 44px; }

  /* Body area list */
  .body-list { position: absolute; left: 72px; top: 1432px; width: 1060px; list-style: none; }
  .body-list li {
    height: 128px; border-bottom: 4px solid var(--rule);
    display: flex; align-items: center; justify-content: space-between;
    padding: 0 16px 0 32px; font-size: 56px; color: var(--text);
  }
  .body-list svg { width: 28px; height: 48px; }

  /* Footer */
  .app-footer {
    position: absolute; left: 0; top: 3192px; width: 1200px; height: 160px;
    background: var(--ink); color: var(--white);
    display: flex; align-items: center; justify-content: center; font-size: 54px;
  }
</style>
</head>
<body>
<div class="screen">
  <header class="app-header">
    <div class="brand"><span class="brand-mark"></span><span class="brand-name">MCH</span></div>
    <h1 class="app-title">Create Exercise Program</h1>
    <svg class="help-icon" viewBox="0 0 120 120" aria-label="Help">
      <circle cx="60" cy="60" r="56" fill="#ffffff"/>
      <text x="60" y="84" text-anchor="middle" font-family="Roboto, Arial, sans-serif" font-weight="700" font-size="76" fill="#000000">?</text>
    </svg>
  </header>

  <section class="step-panel">
    <div class="btn btn-cancel">Cancel</div>
    <div class="step-label">STEP 1 OF 3</div>
    <div class="btn btn-next">Next &gt;</div>
    <div class="btn btn-view">View Program
      <svg viewBox="0 0 64 48"><polygon points="32,2 62,46 2,46" fill="#45c35a"/></svg>
    </div>
    <div class="count-badge">3</div>
    <div class="mode-toggle">
      <span class="mode-option is-active">Rapid</span>
      <span class="mode-option">Keyword | Protocols</span>
    </div>
  </section>

  <div class="field-label" style="left:72px;top:950px;">Libraries:</div>
  <div class="field-label" style="left:624px;top:950px;">Filters:</div>
  <div class="select" style="left:72px;width:500px;">General
    <svg viewBox="0 0 72 44"><polyline points="4,6 36,38 68,6" fill="none" stroke="#555555" stroke-width="7"/></svg>
  </div>
  <div class="select" style="left:624px;width:508px;">All
    <svg viewBox="0 0 72 44"><polyline points="4,6 36,38 68,6" fill="none" stroke="#555555" stroke-width="7"/></svg>
  </div>

  <div class="field-label" style="left:72px;top:1316px;">Body Area:</div>
  <ul class="body-list">
    <li>Face/TMJ<svg viewBox="0 0 28 48"><polyline points="4,4 24,24 4,44" fill="none" stroke="#9a9a9a" stroke-width="5"/></svg></li>
    <li>Cervical<svg viewBox="0 0 28 48"><polyline points="4,4 24,24 4,44" fill="none" stroke="#9a9a9a" stroke-width="5"/></svg></li>
    <li>Thoracic<svg viewBox="0 0 28 48"><polyline points="4,4 24,24 4,44" fill="none" stroke="#9a9a9a" stroke-width="5"/></svg></li>
    <li>Lumbar<svg viewBox="0 0 28 48"><polyline points="4,4 24,24 4,44" fill="none" stroke="#9a9a9a" stroke-width="5"/></svg></li>
    <li>Abdominal<svg viewBox="0 0 28 48"><polyline points="4,4 24,24 4,44" fill="none" stroke="#9a9a9a" stroke-width="5"/></svg></li>
    <li>Sacroliliac<svg viewBox="0 0 28 48"><polyline points="4,4 24,24 4,44" fill="none" stroke="#9a9a9a" stroke-width="5"/></svg></li>
    <li>Hip<svg viewBox="0 0 28 48"><polyline points="4,4 24,24 4,44" fill="none" stroke="#9a9a9a" stroke-width="5"/></svg></li>
    <li>Knee<svg viewBox="0 0 28 48"><polyline points="4,4 24,24 4,44" fill="none" stroke="#9a9a9a" stroke-width="5"/></svg></li>
    <li>Ankle/Foot<svg viewBox="0 0 28 48"><polyline points="4,4 24,24 4,44" fill="none" stroke="#9a9a9a" stroke-width="5"/></svg></li>
    <li>Shoulder<svg viewBox="0 0 28 48"><polyline points="4,4 24,24 4,44" fill="none" stroke="#9a9a9a" stroke-width="5"/></svg></li>
    <li>Elbow<svg viewBox="0 0 28 48"><polyline points="4,4 24,24 4,44" fill="none" stroke="#9a9a9a" stroke-width="5"/></svg></li>
    <li>Wrist/Hand<svg viewBox="0 0 28 48"><polyline points="4,4 24,24 4,44" fill="none" stroke="#9a9a9a" stroke-width="5"/></svg></li>
    <li>All Body<svg viewBox="0 0 28 48"><polyline points="4,4 24,24 4,44" fill="none" stroke="#9a9a9a" stroke-width="5"/></svg></li>
  </ul>

  <footer class="app-footer">Copyrights © 2019, MotionCraft Hub.</footer>
</div>
</body>
</html>
```